Criação de Folder para Logística, Entrega & Armazenamento
" Na grande maioria dos meus negocio, hoje estamos com foco na venda de Gesso Agrícola, Calcário e milho. fazemos negócios com Produtores rurais e granjas. vendemos o gesso e entregamos com a nossa frota de caminhões seja, frota própria ou caminhões agregado. da mesma maneira são os negócios com grãos, originamos os grãos dos produtores e vedemos para as granjas, entregamos com a nossa frota própria ou caminhões agregados. "

```html
<!DOCTYPE html>
<html lang="pt-BR">
<head>
<meta charset="utf-8">
<title>Serra Alta Agro – Folder</title>
<link href="https://fonts.googleapis.com/css2?family=Montserrat:wght@400;500;600;700;800&display=swap" rel="stylesheet">
<style>
  :root{
    --bg:#e7e4df;
    --orange:#e0891c;
    --orange-deep:#c96f0e;
    --green:#0e4536;
    --green-deep:#082e24;
    --paper:#f6f4ef;
    --white:#ffffff;
    --ink:#2b2b2b;
  }
  *{box-sizing:border-box;margin:0;padding:0}
  html,body{width:1200px;height:1200px;overflow:hidden}
  body{background:var(--bg);font-family:"Montserrat",sans-serif;position:relative}
  .page{position:absolute;overflow:hidden}
  .page svg.lines{position:absolute;inset:0;width:100%;height:100%;pointer-events:none}
  .brand{display:flex;align-items:center;gap:10px;font-weight:600;color:var(--white);white-space:nowrap}
  .brand-square{width:22px;height:22px;background:var(--white);flex:none}
  .photo{position:absolute}

  /* inner flap */
  .flap{left:60px;top:140px;width:360px;height:360px;background:var(--paper)}
  .flap .photo-field{inset:0;background:linear-gradient(160deg,#f7f6f2 0%,#ebe7dc 55%,#d9d2bf 100%)}
  .flap .band{position:absolute;left:0;top:0;bottom:0;width:78px;background:var(--orange)}
  .flap .band .brand{position:absolute;left:50%;top:50%;transform:translate(-50%,-50%) rotate(-90deg);font-size:20px}
  .flap .band .brand-square{width:16px;height:16px}
  .flap .items{position:absolute;left:104px;top:44px;right:30px;display:flex;flex-direction:column;gap:34px}
  .item h3{font-size:12px;font-weight:700;color:var(--orange-deep);text-transform:uppercase;margin-bottom:6px;letter-spacing:.3px}
  .item p{font-size:10px;line-height:1.45;color:var(--ink);max-width:170px}

  /* inner fleet page */
  .fleet{left:420px;top:140px;width:360px;height:360px;background:var(--green)}
  .fleet .intro{position:absolute;left:30px;top:34px;width:230px}
  .fleet .intro h3{font-size:13px;font-weight:700;color:var(--orange);text-transform:uppercase;margin-bottom:8px}
  .fleet .intro p{font-size:10px;line-height:1.5;color:#d9e6df}
  .fleet .photo-truck{left:0;right:70px;bottom:0;height:190px;background:linear-gradient(180deg,#8ca3ad 0%,#5e7178 45%,#3b4a46 100%)}

  /* inner trade page */
  .trade{left:780px;top:140px;width:360px;height:360px;background:var(--orange)}
  .trade .photo-tractor{right:0;top:24px;width:170px;height:110px;background:linear-gradient(180deg,#c9d3da 0%,#a8a08a 50%,#7b6a4e 100%)}
  .trade .photo-grain{right:0;bottom:22px;width:170px;height:110px;background:linear-gradient(135deg,#f1c56b 0%,#d99a33 60%,#9c2a22 100%)}
  .trade .mid{position:absolute;left:0;right:0;top:150px;height:60px;background:var(--green)}
  .trade .block{position:absolute;left:24px;width:150px}
  .trade .block h3{font-size:11px;font-weight:700;color:var(--white);text-transform:uppercase;margin-bottom:6px;line-height:1.25}
  .trade .block p{font-size:9.5px;line-height:1.45;color:#fff3e2}
  .trade .block.top{top:40px}
  .trade .block.bottom{top:236px}
  .trade .mid .brand{position:absolute;left:24px;top:50%;transform:translateY(-50%);font-size:14px}
  .trade .mid .brand-square{width:14px;height:14px;background:var(--orange)}

  /* back cover */
  .back{left:60px;top:540px;width:520px;height:520px;background:var(--green)}
  .back .photo-hands{left:0;top:0;width:300px;height:520px;background:radial-gradient(circle at 45% 48%,#5f8f3b 0%,#2e5a2c 30%,#143c2f 65%,var(--green) 100%)}
  .back .brand{position:absolute;left:292px;top:118px;font-size:20px}
  .back .brand-square{background:var(--orange);width:22px;height:22px}
  .back .contact{position:absolute;left:34px;bottom:40px;font-size:11px;line-height:1.7;color:#d9e6df}

  /* front cover */
  .front{left:620px;top:540px;width:520px;height:520px;background:var(--orange)}
  .front .texture{left:0;top:0;width:300px;height:520px;background:linear-gradient(90deg,rgba(201,111,14,.55) 0%,rgba(224,137,28,0) 100%)}
  .front .brand{position:absolute;left:90px;top:82px;font-size:26px}
  .front .brand-square{width:28px;height:28px}
  .front .title{position:absolute;right:44px;bottom:96px;text-align:right;color:var(--white);text-transform:uppercase}
  .front .title .lead{display:block;font-size:30px;font-weight:800;letter-spacing:.5px}
  .front .title .sub{display:block;font-size:17px;font-weight:500;margin-top:4px;letter-spacing:.5px}
</style>
</head>
<body>

<section class="page flap">
  <div class="photo photo-field" role="img" aria-label="Foto clara de lavoura ao fundo"></div>
  <div class="band"><div class="brand"><span class="brand-square"></span>Serra Alta Agro</div></div>
  <div class="items">
    <div class="item"><h3>Gesso Agrícola</h3><p>Correção do solo com entrega direta na fazenda.</p></div>
    <div class="item"><h3>Calcário</h3><p>Qualidade garantida para cada lavoura.</p></div>
    <div class="item"><h3>Milho</h3><p>Originado de produtores parceiros da região.</p></div>
  </div>
</section>

<section class="page fleet">
  <div class="intro">
    <h3>Nossa frota</h3>
    <p>Caminhões próprios e agregados levam sua carga com segurança e pontualidade.</p>
  </div>
  <div class="photo photo-truck" role="img" aria-label="Foto de caminhão graneleiro na estrada"></div>
  <svg class="lines" viewBox="0 0 360 360">
    <rect x="250" y="120" width="80" height="220" rx="22" fill="none" stroke="#ffffff" stroke-width="1.5"/>
    <circle cx="300" cy="60" r="2" fill="#ffffff"/><circle cx="318" cy="80" r="2" fill="#ffffff"/><circle cx="286" cy="92" r="2" fill="#ffffff"/>
  </svg>
</section>

<section class="page trade">
  <div class="photo photo-tractor" role="img" aria-label="Foto de trator trabalhando no campo"></div>
  <div class="block top"><h3>Comercialização de grãos</h3><p>Compramos do produtor e vendemos às granjas.</p></div>
  <div class="mid"><div class="brand"><span class="brand-square"></span>Serra Alta Agro</div></div>
  <div class="block bottom"><h3>Armazenamento e entrega</h3><p>Estrutura pronta para receber e despachar.</p></div>
  <div class="photo photo-grain" role="img" aria-label="Foto de milho sendo descarregado de caminhão"></div>
  <svg class="lines" viewBox="0 0 360 360">
    <path d="M14 140 V20 a12 12 0 0 1 12 -12 H150" fill="none" stroke="#ffffff" stroke-width="1.3"/>
    <path d="M14 222 V340 a12 12 0 0 0 12 12 H150" fill="none" stroke="#ffffff" stroke-width="1.3"/>
  </svg>
</section>

<section class="page back">
  <div class="photo photo-hands" role="img" aria-label="Foto de mãos segurando solo com muda de planta"></div>
  <div class="brand"><span class="brand-square"></span>Serra Alta Agro</div>
  <div class="contact">
    <p>(00) 0000-0000</p>
    <p>contato@serraaltaagro.com.br</p>
    <p>www.serraaltaagro.com.br</p>
  </div>
  <svg class="lines" viewBox="0 0 520 520">
    <rect x="70" y="30" width="200" height="250" rx="28" fill="none" stroke="#e0891c" stroke-width="2"/>
    <rect x="250" y="330" width="230" height="120" rx="24" fill="none" stroke="#ffffff" stroke-width="1.5"/>
    <path d="M300 300 H490" stroke="#e0891c" stroke-width="2"/>
  </svg>
</section>

<section class="page front">
  <div class="photo texture" role="img" aria-label="Textura suave de espigas de trigo em tom laranja"></div>
  <div class="brand"><span class="brand-square"></span>Serra Alta Agro</div>
  <h1 class="title"><span class="lead">Comercialização de</span><span class="sub">Grãos, adubos e gesso agrícola</span></h1>
  <svg class="lines" viewBox="0 0 520 520">
    <rect x="390" y="40" width="96" height="230" rx="26" fill="none" stroke="#ffffff" stroke-width="1.5"/>
    <path d="M40 470 H300 a20 20 0 0 0 20 -20 V440" fill="none" stroke="#ffffff" stroke-width="1.5"/>
    <path d="M520 470 H360" stroke="#ffffff" stroke-width="1.5"/>
    <circle cx="40" cy="60" r="2.5" fill="#ffffff"/><circle cx="58" cy="76" r="2.5" fill="#ffffff"/><circle cx="34" cy="92" r="2.5" fill="#ffffff"/>
  </svg>
</section>

</body>
</html>
```